Header and Full-Page Flyer needed for 2021 Lone Prairie Civic Builders Summit

Save the Date Flyer and Header needed for Q-MarvEt's 2021 Lone Prairie Civic Builders Summit. The Lone Prairie Civic Builders Summit is developed by Owners, for Owners (and other industry stakeholders.

DO NOT INCLUDE This in your design - for reference on design ideas only.
About the The Lone Prairie Civic Builders Summit:

Are you working within the boundaries of a smaller town mentality?
Do you feel stuck within your Big City limits?

The Lone Prairie Civic Builders Summit is where municipalities, counties, ISD's, and other public entities will come together to share what they know, and define what they want to know more about capital project planning design, delivery, and operations.

Font styles to use
Sans Serif

Requirements
Must have
• Lone Prairie Civic Builders Summit
Date: August 5, 2021
Location: San Antonio, TX

```html
<!DOCTYPE html>
<html lang="en">
<head>
<meta charset="UTF-8">
<title>Save the Date – 2021 Lone Prairie Civic Builders Summit</title>
<link rel="stylesheet" href="https://fonts.googleapis.com/css2?family=Montserrat:wght@500;600;700;800&family=Allura&display=swap">
<style>
  :root {
    --page: #ffffff;
    --frame: #6b6b6b;
    --brand-blue: #1f3f94;
    --brand-green: #8cc63f;
    --logo-grey: #5a5a5a;
    --rule-grey: #9a9a9a;
    --sky-top: #2f6fc0;
    --sky-mid: #6fa6dc;
    --city-light: #c99a6e;
    --city-dusk: #6e5a4e;
    --city-low: #2c4534;
    --white: #ffffff;
  }
  * { margin: 0; padding: 0; box-sizing: border-box; }
  html, body {
    width: 1200px; height: 911px; overflow: hidden;
    background: var(--page);
  }
  .canvas { position: relative; width: 1200px; height: 911px; }
  .banner {
    position: absolute; left: 70px; top: 279px;
    width: 1062px; height: 354px;
    border: 1px solid var(--frame);
    background: var(--white);
    overflow: hidden;
    font-family: "Montserrat", Arial, sans-serif;
  }
  .skyline-photo { position: absolute; inset: 0; width: 100%; height: 100%; }

  .brand-dot {
    position: absolute; left: 87px; top: 31px;
    width: 44px; height: 44px; border-radius: 50%;
    background: var(--brand-blue);
  }
  .brand-name {
    position: absolute; left: 153px; top: 30px;
    font-weight: 500; font-size: 32px; line-height: 1;
    color: var(--logo-grey); letter-spacing: 0.3px;
  }
  .brand-rule {
    position: absolute; left: 155px; top: 66px;
    width: 126px; height: 1px; background: var(--rule-grey);
  }
  .event-name {
    position: absolute; left: 155px; top: 70px;
    font-weight: 600; font-size: 9.5px; line-height: 1;
    color: var(--brand-green); white-space: nowrap;
  }

  .headline-script {
    position: absolute; left: 89px; top: 105px;
    font-family: "Allura", cursive;
    font-size: 130px; line-height: 1;
    color: var(--brand-green);
  }
  .headline-main {
    position: absolute; left: 57px; top: 202px;
    font-weight: 700; font-size: 64px; line-height: 1;
    color: var(--brand-blue); letter-spacing: -0.5px;
    white-space: nowrap;
  }

  .location {
    position: absolute; left: 27px; top: 292px;
    width: 384px; height: 41px;
    background: var(--brand-blue);
    display: flex; align-items: center; gap: 8px;
    padding-left: 14px;
    color: var(--white);
  }
  .location-label { font-weight: 600; font-size: 18px; }
  .location-city { font-weight: 700; font-size: 23px; }

  .event-date {
    position: absolute; left: 629px; top: 23px;
    height: 121px;
    padding-left: 14px;
    border-left: 2px solid var(--white);
    color: var(--white);
    line-height: 1;
  }
  .event-day { font-weight: 700; font-size: 80px; letter-spacing: 1px; margin-top: -6px; }
  .event-month { font-weight: 700; font-size: 26px; margin-top: 0; }
  .event-year { font-weight: 700; font-size: 25px; margin-top: 6px; }
</style>
</head>
<body>
<div class="canvas">
  <section class="banner">
    <svg class="skyline-photo" viewBox="0 0 1062 354" role="img" aria-label="Photograph of the San Antonio downtown skyline at dusk with lit towers and trees">
      <defs>
        <linearGradient id="skyline-tones" x1="0" y1="0" x2="0" y2="1">
          <stop offset="0" stop-color="var(--sky-top)"/>
          <stop offset="0.42" stop-color="var(--sky-mid)"/>
          <stop offset="0.62" stop-color="var(--city-light)"/>
          <stop offset="0.8" stop-color="var(--city-dusk)"/>
          <stop offset="1" stop-color="var(--city-low)"/>
        </linearGradient>
      </defs>
      <polygon fill="url(#skyline-tones)" points="
        540,0 1062,0 1062,354 480,354 455,320 470,300 440,285 460,262
        420,238 445,220 400,190 430,172 392,160 440,150 470,130
        438,120 505,95 480,82 540,70 515,58 560,45 535,30 575,22 545,8"/>
    </svg>

    <span class="brand-dot"></span>
    <span class="brand-name">Q-MarvEt</span>
    <span class="brand-rule"></span>
    <span class="event-name">2021 Lone Prairie Civic Builders Summit</span>

    <span class="headline-script">Save</span>
    <span class="headline-main">THE DATE</span>

    <div class="location">
      <svg width="14" height="20" viewBox="0 0 14 20" aria-hidden="true">
        <path d="M7 0C3.1 0 0 3.1 0 7c0 5 7 13 7 13s7-8 7-13c0-3.9-3.1-7-7-7zm0 9.6A2.6 2.6 0 1 1 7 4.4a2.6 2.6 0 0 1 0 5.2z" fill="var(--brand-green)"/>
      </svg>
      <span class="location-label">LOCATION:</span>
      <span class="location-city">SAN ANTONIO, TX</span>
    </div>

    <div class="event-date">
      <div class="event-day">05</div>
      <div class="event-month">August</div>
      <div class="event-year">2021</div>
    </div>
  </section>
</div>
</body>
</html>
```